Catchy Cards for Hospital

I run a rural hospital in Texas called Pelham Ridge Hospital and am in need of contemporary business cards for all of my Department Heads. While our logo is somewhat simplistic, I don't have the option of changing it at this time, so anything to make the rest of the card present the appearance of a modern, professional healthcare facility would be great. Although the attached files are in black, our hospital colors are in a copper brown and black. I need to be able to change the name and title on the card so I can get cards printed for various department heads.

Target Market(s)

Referring physicians, large hospital systems, national organizations, state and federal government

Industry/Entity Type

Hospital

Contact Information for Business Card

Name Derek Solano
Title CEO

Phone: Main 325-740-2386 & Direct xxxxxx
Fax xxxxx
derek.solano@pelhamrh.com
382 Wilmot Street Box 415
Harlan Creek, Texas 76291

Font styles to use
Serif

Colors
f48340

Requirements
Must have
• Clean crisp lines and ability to modify names, titles and emails
• On the back "PelhamRidgeHospital.Com
Nice to have
• Needs to be in line with logo, which is a bit dated and not too appealing, but I'm hoping that the rest of the card can make up for that fact just a little bit.
• Hospital's colors are a copper brown, black and white
Should not have
• Shapes or anything distracting

```html
<!DOCTYPE html>
<html lang="en">
<head>
<meta charset="utf-8">
<title>Pelham Ridge Hospital – Business Card</title>
<link rel="stylesheet" href="https://fonts.googleapis.com/css2?family=Noto+Serif:wght@400;700&display=swap">
<style>
  :root {
    --copper: #f48340;
    --card-black: #000000;
    --ink-white: #ffffff;
    --backdrop: #e4e4e6;
    --card-shadow: rgba(0, 0, 0, 0.28);
  }
  html, body {
    margin: 0;
    padding: 0;
    width: 1200px;
    height: 900px;
    overflow: hidden;
    background: var(--backdrop);
    font-family: "Noto Serif", Georgia, serif;
  }
  .stage {
    position: relative;
    width: 1200px;
    height: 900px;
  }
  .card {
    position: absolute;
    width: 700px;
    height: 400px;
    background: var(--card-black);
    box-shadow: 0 10px 28px var(--card-shadow);
    color: var(--ink-white);
  }
  /* Back side */
  .card--back {
    left: 80px;
    top: 50px;
  }
  .web-address {
    position: absolute;
    left: 0;
    right: 0;
    top: 168px;
    text-align: center;
    font-size: 22px;
    letter-spacing: 0.5px;
    margin: 0;
  }
  .web-address .domain-name { color: var(--copper); }

  /* Front side */
  .card--front {
    left: 420px;
    top: 450px;
  }
  .brand {
    position: absolute;
    left: 50px;
    top: 110px;
    width: 270px;
    display: flex;
    align-items: center;
    gap: 14px;
  }
  .brand-dot {
    flex: 0 0 auto;
    width: 22px;
    height: 22px;
    border-radius: 50%;
    background: var(--copper);
  }
  .brand-name {
    margin: 0;
    color: var(--copper);
    font-weight: 700;
    font-size: 30px;
    line-height: 1.12;
  }
  .divider {
    position: absolute;
    left: 345px;
    top: 70px;
    width: 1.5px;
    height: 240px;
    background: var(--copper);
  }
  .contact {
    position: absolute;
    left: 375px;
    top: 68px;
    right: 20px;
  }
  .person-name {
    margin: 0;
    color: var(--copper);
    font-weight: 700;
    font-size: 24px;
    letter-spacing: 0.5px;
  }
  .person-title {
    margin: 0 0 22px;
    font-size: 16px;
  }
  .address {
    margin: 0 0 12px;
    font-style: normal;
    font-size: 16px;
    line-height: 1.35;
  }
  .contact-list {
    list-style: none;
    margin: 0;
    padding: 0;
    font-size: 16px;
  }
  .contact-list li {
    display: flex;
    align-items: center;
    gap: 12px;
    height: 24px;
  }
  .contact-icon {
    width: 20px;
    height: 20px;
    flex: 0 0 auto;
  }
</style>
</head>
<body>
<main class="stage">

  <section class="card card--back" aria-label="Card back">
    <p class="web-address">www.<span class="domain-name">PelhamRidgeHospital</span>.Com</p>
  </section>

  <section class="card card--front" aria-label="Card front">
    <div class="brand">
      <span class="brand-dot"></span>
      <p class="brand-name">Pelham Ridge Hospital</p>
    </div>

    <div class="divider"></div>

    <div class="contact">
      <p class="person-name">Derek Solano</p>
      <p class="person-title">CEO</p>
      <address class="address">382 Wilmot Street Box 415<br>Harlan Creek, Texas 76291</address>
      <ul class="contact-list">
        <li>
          <svg class="contact-icon" viewBox="0 0 20 20" aria-label="Main phone">
            <rect width="20" height="20" rx="4" fill="var(--copper)"/>
            <path d="M4 8 Q10 3 16 8 L14 10 L12 8.5 L8 8.5 L6 10 Z M6 11 H14 V15 H6 Z" fill="#000"/>
          </svg>
          325-740-2386
        </li>
        <li>
          <svg class="contact-icon" viewBox="0 0 20 20" aria-label="Direct line">
            <rect width="20" height="20" rx="4" fill="var(--copper)"/>
            <path d="M6 4 L9 4 L10 7 L8.5 8.5 Q10 11.5 11.5 12 L13 10.5 L16 11.5 L16 14.5 Q10 16 6 11 Q4 7 6 4 Z" fill="#000"/>
          </svg>
          123-456-789
        </li>
        <li>
          <svg class="contact-icon" viewBox="0 0 20 20" aria-label="Fax">
            <rect width="20" height="20" rx="4" fill="var(--copper)"/>
            <rect x="6" y="3.5" width="8" height="4" fill="#000"/>
            <rect x="3.5" y="8" width="13" height="6" rx="1" fill="#000"/>
            <rect x="6" y="12.5" width="8" height="4" fill="#000"/>
          </svg>
          123-456-789
        </li>
        <li>
          <svg class="contact-icon" viewBox="0 0 20 20" aria-label="Email">
            <rect width="20" height="20" rx="4" fill="var(--copper)"/>
            <rect x="3.5" y="5.5" width="13" height="9" fill="none" stroke="#000" stroke-width="1.4"/>
            <path d="M3.5 5.5 L10 11 L16.5 5.5" fill="none" stroke="#000" stroke-width="1.4"/>
          </svg>
          derek.solano@pelhamrh.com
        </li>
      </ul>
    </div>
  </section>

</main>
</body>
</html>
```